Plumbing Company trying to attract new client base for particular works

In need of something to letterbox drop. There is an opportunity to provide "new sewer drains to the new sewer connections on your street".
There will be discounts for pensioners.
We have reviews from clients that are highly satisfied with our work.
Work booked within 1 months of stamped date on flyer will receive a further 10% off.
All work carried out by licences tradespeople.

LOGO will need to be altered to say "tidewell plumbing" rather than contracting

Target Market(s)

Home owners in regional South Australia - age 30+

Industry/Entity Type

It Company

Requirements
Must have
• contact phone number, email, company name,
Nice to have
• images,

```html
<!DOCTYPE html>
<html lang="en">
<head>
<meta charset="utf-8">
<title>Tidewell Plumbing – New Sewer Drains Flyer</title>
<link href="https://fonts.googleapis.com/css2?family=Teko:wght@500;600&family=Lato:wght@700;900&family=Montserrat:wght@600;800&display=swap" rel="stylesheet">
<style>
  :root{
    --ink:#0d0d0d;
    --ink-soft:#1c1c1c;
    --yellow:#f6cc1d;
    --yellow-deep:#e9b80c;
    --white:#ffffff;
    --photo-dark:#5b4a3a;
    --photo-mid:#8a7560;
    --photo-sky:#c9c7c2;
  }
  *{margin:0;padding:0;box-sizing:border-box}
  html,body{width:899px;height:1200px;overflow:hidden;background:#ddd}
  .flyer{
    position:relative;width:899px;height:1200px;overflow:hidden;
    background:radial-gradient(ellipse at 60% 55%, #2d2416 0%, var(--ink-soft) 40%, var(--ink) 75%);
  }
  .flyer__art{position:absolute;left:0;top:0}
  .brand{
    position:absolute;left:588px;top:150px;width:240px;
    display:flex;align-items:center;gap:12px;
    font-family:"Montserrat",sans-serif;font-weight:800;color:var(--ink);
  }
  .brand__mark{width:38px;height:38px;background:var(--yellow);flex:none}
  .brand__name{font-size:29px;line-height:1;letter-spacing:1px}
  .brand__name small{display:block;font-size:12px;letter-spacing:5px;margin-top:6px}
  .headline{
    position:absolute;left:0;width:899px;text-align:center;white-space:nowrap;
    font-family:"Teko",sans-serif;text-transform:uppercase;line-height:1;
  }
  .headline--lead{top:712px;color:var(--yellow);font-size:44px;font-weight:500}
  .headline--main{top:764px;color:var(--white);font-size:138px;font-weight:600;letter-spacing:1px}
  .offer{
    position:absolute;left:42px;white-space:nowrap;
    font-family:"Lato",sans-serif;font-weight:900;text-transform:uppercase;
    color:var(--yellow);line-height:1;
  }
  .offer--first{top:906px;font-size:23px;font-weight:700}
  .offer--second{top:936px;font-size:31px}
  .offer em{font-style:normal;color:var(--white)}
  .reviews{
    position:absolute;left:40px;top:1028px;white-space:nowrap;
    font-family:"Teko",sans-serif;font-weight:500;font-size:26px;
    color:var(--ink);text-transform:uppercase;line-height:1;
  }
  .contact{
    position:absolute;left:47px;top:1116px;display:flex;gap:38px;white-space:nowrap;
    font-family:"Teko",sans-serif;font-weight:500;font-size:29px;color:var(--white);
    text-transform:uppercase;line-height:1;
  }
  .contact__item{display:flex;align-items:center;gap:12px}
  .contact__item svg{width:22px;height:22px}
</style>
</head>
<body>
<main class="flyer">
  <svg class="flyer__art" width="899" height="1200" viewBox="0 0 899 1200">
    <defs>
      <linearGradient id="photoMain" x1="0" y1="0" x2="1" y2="1">
        <stop offset="0" stop-color="var(--photo-sky)"/>
        <stop offset=".5" stop-color="var(--photo-mid)"/>
        <stop offset="1" stop-color="var(--photo-dark)"/>
      </linearGradient>
      <linearGradient id="photoTrench" x1="0" y1="0" x2="0" y2="1">
        <stop offset="0" stop-color="#7c8a5a"/>
        <stop offset="1" stop-color="#6a4e36"/>
      </linearGradient>
      <linearGradient id="groundFill" x1="0" y1="0" x2="1" y2="1">
        <stop offset="0" stop-color="var(--yellow)"/>
        <stop offset="1" stop-color="var(--yellow-deep)"/>
      </linearGradient>
    </defs>

    <path d="M0 0 H899 V360 L560 640 Q300 520 0 500 Z" fill="var(--white)"/>

    <path d="M0 0 H640 L470 300 Q420 420 380 470 Q250 430 0 460 Z" fill="url(#photoMain)"
          role="img" aria-label="Photo of an operator on a red mini excavator digging beside a brick house"/>

    <path d="M0 500 Q260 430 470 560" fill="none" stroke="var(--white)" stroke-width="34"/>
    <path d="M0 540 Q260 470 500 600" fill="none" stroke="var(--yellow)" stroke-width="18"/>

    <rect x="770" y="290" width="230" height="230" rx="34" transform="rotate(45 885 405)" fill="var(--yellow)"/>

    <rect x="590" y="40" width="260" height="260" rx="40" transform="rotate(45 720 170)" fill="var(--yellow)"/>
    <rect x="604" y="54" width="232" height="232" rx="34" transform="rotate(45 720 170)" fill="var(--ink)"/>
    <rect x="616" y="66" width="208" height="208" rx="28" transform="rotate(45 720 170)" fill="var(--white)"/>

    <rect x="395" y="300" width="190" height="190" rx="30" transform="rotate(45 490 395)" fill="var(--ink)"/>
    <rect x="405" y="310" width="170" height="170" rx="24" transform="rotate(45 490 395)" fill="var(--yellow)"/>
    <rect x="413" y="318" width="154" height="154" rx="20" transform="rotate(45 490 395)" fill="url(#photoTrench)"
          role="img" aria-label="Photo of a freshly dug sewer trench with a pipe in a garden"/>

    <rect x="605" y="480" width="210" height="210" rx="32" transform="rotate(45 710 585)" fill="var(--ink)"/>
    <rect x="615" y="490" width="190" height="190" rx="26" transform="rotate(45 710 585)" fill="var(--yellow)"/>
    <rect x="623" y="498" width="174" height="174" rx="22" transform="rotate(45 710 585)" fill="url(#photoTrench)"
          role="img" aria-label="Photo of a sewer connection trench with exposed pipe beside a skip bin"/>

    <path d="M0 1012 H790 L760 1068 H0 Z" fill="var(--yellow)"/>

    <path d="M899 870 V1200 H660 Z" fill="url(#groundFill)"
          role="img" aria-label="Textured yellow ground surface"/>
    <path d="M899 858 L652 1200 H640 L899 842 Z" fill="var(--white)"/>
  </svg>

  <div class="brand">
    <span class="brand__mark"></span>
    <span class="brand__name">TIDEWELL<small>PLUMBING</small></span>
  </div>

  <h2 class="headline headline--lead">New sewer drains to the new sewer connections</h2>
  <h1 class="headline headline--main">On your street</h1>

  <p class="offer offer--first">Work booked within <em>1 months</em> of stamped date</p>
  <p class="offer offer--second">On flyer will receive a further <em>10% off</em></p>

  <p class="reviews">We have reviews from clients that are highly satisfied with our work</p>

  <div class="contact">
    <span class="contact__item">
      <svg viewBox="0 0 24 24" aria-hidden="true"><path fill="var(--white)" d="M6.6 10.8a15.1 15.1 0 0 0 6.6 6.6l2.2-2.2c.3-.3.7-.4 1-.2 1.1.4 2.3.6 3.6.6.6 0 1 .4 1 1V20c0 .6-.4 1-1 1A17 17 0 0 1 3 4c0-.6.4-1 1-1h3.5c.6 0 1 .4 1 1 0 1.3.2 2.5.6 3.6.1.3 0 .7-.2 1z"/></svg>
      0123456789
    </span>
    <span class="contact__item">
      <svg viewBox="0 0 24 24" aria-hidden="true"><rect x="2" y="5" width="20" height="14" fill="none" stroke="var(--white)" stroke-width="2"/><path d="M2 5l10 8 10-8" fill="none" stroke="var(--white)" stroke-width="2"/></svg>
      companyname@domainname.com
    </span>
  </div>
</main>
</body>
</html>
```